Bright Harbour Fitness

BRIGHT HARBOUR FITNESS PTY LTD, We are a revolutionary, fresh, new entity to the fitness industry looking to make a mark within and support local communities where we are situated. My business partner and i come with a broad range of skill sets and possess the ability and motivation to ensure our philosophy works - and the philosophy is simple - to help people improve their everyday life and well-being. Be it, helping them with their health and fitness, changing their appearance, improving motivation, setting and achieving goals or by helping them become part of a positive team atmosphere.
Our stores visual appearance, like our training concepts, is quite different to the normal run of the mill gym. It's fresh, it's vibrant, it looks great, and we know it will be a real head turner guaranteed to attract attention. This is definitely the future of fitness.
We would like to see on one side our Info and on the other side our LOGO, colour scheme is in the LOGO.
Final design should tell people "We Help People Look And Feel Bright As The Harbour!

Industry/Entity Type

Training

Contact Information for Business Card

Corwin
0412 386 054
cor@brightharbourfitness.com.au
217 Kestrelvale Rd Wattle Cove NSW 2188

Requirements
Must have
• Our Logo

```html
<!DOCTYPE html>
<html lang="en">
<head>
<meta charset="utf-8">
<title>Bright Harbour Fitness – Business Card</title>
<link rel="stylesheet" href="https://fonts.googleapis.com/css2?family=Share+Tech+Mono&display=swap">
<style>
  :root {
    --page-bg: #ece8e1;
    --red: #e4232b;
    --yellow: #ece526;
    --green: #9cc83e;
    --blue: #2492d1;
    --slate: #34474d;
    --slate-band: #4d6a70;
    --ink: #2e3a3f;
    --white: #ffffff;
    --card-shadow: 0 10px 28px rgba(40, 35, 25, 0.22);
  }
  * { box-sizing: border-box; margin: 0; padding: 0; }
  html, body {
    width: 1200px;
    height: 1000px;
    overflow: hidden;
    background: var(--page-bg);
    font-family: "Share Tech Mono", monospace;
  }
  .canvas {
    position: relative;
    width: 1200px;
    height: 1000px;
  }
  .card {
    position: absolute;
    left: 260px;
    width: 680px;
    height: 425px;
    overflow: hidden;
    box-shadow: var(--card-shadow);
    background: var(--white);
  }
  .card--front { top: 50px; }
  .card--back  { top: 525px; }

  .pattern-fill {
    position: absolute;
    left: 0;
    right: 0;
    background:
      linear-gradient(120deg,
        rgba(255,255,255,0) 0%, rgba(255,255,255,0.18) 50%, rgba(255,255,255,0) 100%),
      linear-gradient(115deg,
        var(--blue) 0%, var(--yellow) 28%, var(--green) 52%, var(--red) 78%, var(--blue) 100%);
  }
  .card--front .pattern-fill { top: 0; bottom: 0; }
  .card--back .pattern-fill { top: 0; height: 230px; }

  .brand {
    position: absolute;
    top: 150px;
    left: 40px;
    display: flex;
    align-items: center;
    gap: 18px;
  }
  .brand__mark {
    width: 62px;
    height: 62px;
    background: var(--white);
  }
  .brand__name {
    font-size: 38px;
    letter-spacing: 1px;
    color: var(--ink);
    white-space: nowrap;
  }

  .back-strip {
    position: absolute;
    top: 230px;
    left: 0;
    right: 0;
    height: 8px;
    background: var(--slate-band);
  }
  .back-panel {
    position: absolute;
    top: 238px;
    left: 0;
    right: 0;
    bottom: 0;
    background: var(--slate);
    color: var(--white);
  }
  .contact-name {
    position: absolute;
    top: 16px;
    left: 38px;
    font-size: 32px;
    letter-spacing: 2px;
  }
  .contact-list {
    position: absolute;
    top: 30px;
    right: 30px;
    list-style: none;
    text-align: right;
    font-size: 17px;
    line-height: 25px;
  }
  .contact-list li::before {
    content: "";
    display: inline-block;
    width: 9px;
    height: 9px;
    margin-right: 10px;
    background: var(--white);
    vertical-align: 1px;
  }
</style>
</head>
<body>
<main class="canvas">

  <section class="card card--front" aria-label="Business card front">
    <div class="pattern-fill" role="img" aria-label="Colourful triangle mosaic in red, yellow, green and blue"></div>
    <div class="brand">
      <span class="brand__mark"></span>
      <span class="brand__name">BRIGHT HARBOUR FITNESS</span>
    </div>
  </section>

  <section class="card card--back" aria-label="Business card back">
    <div class="pattern-fill" role="img" aria-label="Colourful triangle mosaic in red, yellow, green and blue"></div>
    <div class="back-strip"></div>
    <div class="back-panel">
      <p class="contact-name">Corwin</p>
      <ul class="contact-list">
        <li>0412 386 054</li>
        <li>cor@brightharbourfitness.com.au</li>
        <li>217 Kestrelvale Rd Wattle Cove</li>
        <li>NSW 2188</li>
      </ul>
    </div>
  </section>

</main>
</body>
</html>
```